out of the box Business Card Design for a Manufacturer / Distributor

We are a manufarturer and distributor of products.
the company name is VORTANI (Pic attached)

the picture is NOT a must have on the business Card.

the Business Card should look really professional and/or special, so out of the box thinking is welcome.

there should be 2 Adresses on the Business Card for Main and Branch Office.
Email Adress, homepage, Name is required
NO Phone Number

Our working field:
Private Labeling
high Quality Production
direct distribution
warehousing
trademark registration
legal support

Main Office:
Kornblumenweg 14
08352 Halvenstedt
Germany

Branch Office:
Daska Lane
Zarenpur
Pakistan

Names:
Lukas Feldhaus (Owner)
Imran Qureshi (Owner)

Email:
lukas@vortani-example.com
imran@vortani-example.com

homepage:
vortani-example.com

Industry/Entity Type

Manufacturer Distributer

Contact Information for Business Card

Vortani

Requirements
Must have
• Names, both office Adresses, email, homepage
Should not have
• Phone Number

```html
<!DOCTYPE html>
<html lang="en">
<head>
<meta charset="utf-8">
<title>Vortani Business Card</title>
<link rel="stylesheet" href="https://fonts.googleapis.com/css2?family=Karla:ital,wght@0,400;0,600;0,700;1,400&display=swap">
<style>
  :root {
    --backdrop: #999999;
    --card-dark: #484848;
    --card-light: #ffffff;
    --band: #d9d9d9;
    --ink-light: #f2f2f2;
    --ink-dark: #454545;
    --rule: #8a8a8a;
  }
  * { box-sizing: border-box; margin: 0; padding: 0; }
  html, body {
    width: 1133px; height: 1200px; overflow: hidden;
    background: var(--backdrop);
    font-family: "Karla", Arial, sans-serif;
  }
  .canvas { position: relative; width: 1133px; height: 1200px; }
  .card {
    position: absolute; left: 197px; width: 724px; height: 412px;
    border-radius: 22px; overflow: hidden;
  }
  .card--front { top: 144px; background: var(--card-dark); color: var(--ink-light); }
  .card--back { top: 640px; background: var(--card-light); }

  .owners {
    position: absolute; right: calc(724px - 336px); top: 130px;
    text-align: right;
  }
  .owners__name {
    font-weight: 700; font-size: 23px; letter-spacing: 0.6px; line-height: 25px;
    text-transform: uppercase;
  }
  .owners__role { font-style: italic; font-size: 14px; margin-top: 6px; }

  .divider {
    position: absolute; left: 362px; top: 59px; width: 1.5px; height: 211px;
    background: var(--rule);
  }

  .contact { position: absolute; left: 386px; top: 69px; font-size: 15.5px; line-height: 19px; letter-spacing: 0.3px; }
  .contact__heading { font-weight: 700; text-transform: uppercase; }
  .contact__block + .contact__block { margin-top: 2px; }
  .contact__list { list-style: none; margin-top: 2px; }
  .contact__item { display: flex; align-items: center; gap: 10px; height: 20px; }
  .contact__icon { width: 12px; height: 12px; fill: var(--ink-light); flex: none; }

  .fields {
    position: absolute; left: 0; top: 298px; width: 100%; height: 78px;
    background: var(--band); color: var(--ink-dark); text-align: center;
    padding-top: 6px; font-size: 16px; line-height: 20px; letter-spacing: 0.3px;
  }
  .fields__heading { font-weight: 700; text-transform: uppercase; font-size: 15.5px; }

  .brand {
    position: absolute; left: 146px; top: 140px; height: 130px;
    display: flex; align-items: center; gap: 20px; color: var(--ink-dark);
  }
  .brand__dot { width: 100px; height: 100px; border-radius: 50%; background: var(--ink-dark); }
  .brand__name { font-size: 76px; font-weight: 400; letter-spacing: 5px; line-height: 1; }
</style>
</head>
<body>
<main class="canvas">
  <section class="card card--front">
    <div class="owners">
      <p class="owners__name">Lukas Feldhaus</p>
      <p class="owners__name">Imran Qureshi</p>
      <p class="owners__role">Owner</p>
    </div>
    <div class="divider"></div>
    <div class="contact">
      <div class="contact__block">
        <p class="contact__heading">Main Office</p>
        <p>Kornblumenweg 14</p>
        <p>08352 Halvenstedt, Germany</p>
      </div>
      <div class="contact__block">
        <p class="contact__heading">Branch Office</p>
        <p>Daska Lane</p>
        <p>Zarenpur, Pakistan</p>
      </div>
      <ul class="contact__list">
        <li class="contact__item">
          <svg class="contact__icon" viewBox="0 0 24 24"><path d="M6.6 10.8a15.1 15.1 0 0 0 6.6 6.6l2.2-2.2c.3-.3.7-.4 1-.2 1.1.4 2.3.6 3.6.6.6 0 1 .4 1 1V20c0 .6-.4 1-1 1A17 17 0 0 1 3 4c0-.6.4-1 1-1h3.5c.6 0 1 .4 1 1 0 1.3.2 2.5.6 3.6.1.3 0 .7-.2 1z"/></svg>
          <span>lukas@vortani-example.com</span>
        </li>
        <li class="contact__item">
          <svg class="contact__icon" viewBox="0 0 24 24"><path d="M2 5h20v14H2z M2 5l10 7 10-7" stroke="#484848" stroke-width="2"/></svg>
          <span>imran@vortani-example.com</span>
        </li>
        <li class="contact__item">
          <svg class="contact__icon" viewBox="0 0 24 24"><circle cx="12" cy="12" r="10"/><path d="M2 12h20M12 2c3 3 3 17 0 20M12 2c-3 3-3 17 0 20" stroke="#484848" stroke-width="1.5" fill="none"/></svg>
          <span>www.vortani-example.com</span>
        </li>
      </ul>
    </div>
    <div class="fields">
      <p class="fields__heading">Our Working Field</p>
      <p>Private Labeling •High Quality Production • Direct distribution</p>
      <p>Warehousing •Trademark registration • Legal support</p>
    </div>
  </section>

  <section class="card card--back">
    <div class="brand">
      <span class="brand__dot"></span>
      <span class="brand__name">VORTANI</span>
    </div>
  </section>
</main>
</body>
</html>
```